Tequila Bottle Labels

We are a construction company that bottled our own tequila and would like a unique label for it! We already have our own company logo (linked below) and we want that logo somewhere on the bottle as well- it can be big or small. It was brewed & bottled in Southern California. Ideally it would have the year "2020," "Single Estate," & "100% Agave Azul" somewhere on the label.

Logo Text

Tequila / MTR / 2020

```html
<!DOCTYPE html>
<html lang="en">
<head>
<meta charset="utf-8">
<title>MTR Single Estate Tequila Label</title>
<link rel="stylesheet" href="https://fonts.googleapis.com/css2?family=DM+Serif+Display&family=Rye&family=Oswald:wght@500&family=Playfair+Display:wght@400&display=swap">
<style>
  :root {
    --backdrop: #e9e9e9;
    --label-black: #1f1f1f;
    --label-edge: #f4efe6;
    --gold: #c9a46a;
    --gold-deep: #9c7a47;
    --cream: #f5f1ea;
    --agave: #8a8f93;
  }
  html, body {
    margin: 0;
    padding: 0;
    width: 1200px;
    height: 1027px;
    overflow: hidden;
    background: var(--backdrop);
  }
  .canvas {
    width: 1200px;
    height: 1027px;
    display: flex;
    align-items: center;
    justify-content: center;
  }
  .label { width: 690px; height: 870px; display: block; }
  .label-body { fill: var(--label-black); stroke: var(--label-edge); stroke-width: 3; }
  .gold-frame { fill: none; stroke: var(--gold); stroke-width: 2; }
  .brand-name { font-family: "DM Serif Display", serif; font-size: 78px; fill: var(--cream); }
  .vintage { font-family: "Playfair Display", serif; font-size: 12px; fill: var(--cream); letter-spacing: 1px; }
  .estate { font-family: "Rye", serif; font-size: 11.5px; fill: var(--cream); letter-spacing: 1px; }
  .rule { stroke: var(--cream); stroke-width: 1; }
  .banner-body { fill: var(--label-black); stroke: var(--gold); stroke-width: 2; }
  .banner-inner { fill: none; stroke: var(--cream); stroke-width: 1; }
  .product-name { font-family: "Rye", serif; font-size: 70px; fill: var(--gold); letter-spacing: 1px; }
  .agave-tag { fill: var(--label-black); stroke: var(--gold); stroke-width: 2; }
  .agave-tag-inner { fill: none; stroke: var(--cream); stroke-width: 1.2; }
  .agave-text { font-family: "Rye", serif; font-size: 15px; fill: var(--cream); letter-spacing: 1px; }
  .agave-art { fill: var(--agave); opacity: 0.55; }
  .horizon { fill: none; stroke: var(--gold); stroke-width: 2.5; }
  .origin-small { font-family: "Oswald", sans-serif; font-size: 13px; fill: var(--cream); }
  .origin-large { font-family: "Oswald", sans-serif; font-size: 19px; fill: var(--cream); }
  .volume { font-family: "Playfair Display", serif; font-size: 15px; fill: var(--cream); }
</style>
</head>
<body>
<main class="canvas">
  <svg class="label" viewBox="-5 -5 470 590" xmlns="http://www.w3.org/2000/svg" aria-label="MTR Single Estate Tequila label">
    <path class="label-body" d="M230,0 L430,70 L430,195 L445,210 L445,245 L460,275 L445,305 L445,340 L430,355 L400,360 L400,490 L230,580 L60,490 L60,360 L30,355 L15,340 L15,305 L0,275 L15,245 L15,210 L30,195 L30,70 Z"/>
    <path class="gold-frame" d="M230,12 L418,78 L418,200 L386,204 L386,370 L388,484 L230,566 L72,484 L74,370 L74,204 L42,200 L42,78 Z"/>

    <text class="brand-name" x="230" y="135" text-anchor="middle">MTR</text>
    <text class="vintage" x="230" y="162" text-anchor="middle">2020</text>

    <line class="rule" x1="188" y1="175" x2="272" y2="175"/>
    <text class="estate" x="230" y="195" text-anchor="middle">SINGLE ESTATE</text>
    <line class="rule" x1="188" y1="203" x2="272" y2="203"/>
    <line class="rule" x1="110" y1="190" x2="150" y2="190"/>
    <line class="rule" x1="310" y1="190" x2="350" y2="190"/>

    <path class="banner-body" d="M40,212 L420,212 L420,228 L440,248 L448,275 L440,302 L420,322 L420,338 L40,338 L40,322 L20,302 L12,275 L20,248 L40,228 Z"/>
    <path class="banner-inner" d="M48,220 L412,220 L412,233 L430,252 L437,275 L430,298 L412,317 L412,330 L48,330 L48,317 L30,298 L23,275 L30,252 L48,233 Z"/>
    <text class="product-name" x="230" y="302" text-anchor="middle">TEQUILA</text>

    <path class="agave-tag" d="M124,334 L336,334 L350,352 L336,370 L124,370 L110,352 Z"/>
    <path class="agave-tag-inner" d="M130,339 L330,339 L342,352 L330,365 L130,365 L118,352 Z"/>
    <text class="agave-text" x="230" y="358" text-anchor="middle">100% AGAVE AZUL</text>

    <rect class="agave-art" x="145" y="383" width="170" height="34" role="img" aria-label="Line illustration of an agave plant on the horizon"/>
    <path class="horizon" d="M145,404 Q230,470 315,404"/>

    <text class="origin-small" x="230" y="470" text-anchor="middle">BREWED AND BOTTLED IN</text>
    <text class="origin-large" x="230" y="494" text-anchor="middle">SOUTHERN CALIFORNIA</text>
    <text class="volume" x="230" y="532" text-anchor="middle">700ml</text>
  </svg>
</main>
</body>
</html>
```